Brisk Mend's Blow Their Mind Website

We own a group of cell phone and tablet repair shops in the bay area that is emerging into the mobile device insurance industry and want to develop a site that is clean, organized, and efficient at communicating who we are, the services we provide and the positive feedback we have been getting from our clients. As we enter into this new field of business, Our goal is to attract larger corporate accounts.

We want our home screen to have a big focus on the protection plan for the devices right away much like the home screen from these links:

http://www.gadgetvault.com/

and also - https://us.keepitsnug.com/smartphone-protection.html

We also need to make our repair services clear, here is a website of a company that does repair and we want to highlight both ends of the business.

ww.fixnovo.com

So the home screen will include the tab categories at the top of the screen
home/ protection /repair /about /contact

The first portion will be protection and as you scroll down there will be the next section about repair and following that will be information about the company.

Target Market(s)

Individuals that would be looking for pricing, clients that come to our store, but ultimately the heavy hitters we would want to attract would be larger corporate accounts so the message we want to communicate is professional, organized and credible in the services we provide.

Industry/Entity Type

Cell Phone

Number of Pages Required

5+ page

Font styles to use
Serif

Colors
34a6d7

Requirements
Must have
• Eye catching, organized, with the wow factor that a business will look at our site and will be able to tell that we know what looks good and what grabs peoples attention. A large emphasis on the protection plan section like the links we provided and an organized home screen with the sections highlighted in the project description
• Tabs with links to different sections of the business such as protection that will go into detail about our protections plans and why our plan is best
• repair with a menu of the different prices we provide for different devices and services for that device
• an about us tab
• a contact us tab
Nice to have
• Artistic flow on the homescreen that the different sections flow together without looking too cookie cutter
• Wow factor
Should not have
• Clutter, confusion, disorganization, cheesy cookie cutter

```html
<!DOCTYPE html>
<html lang="en">
<head>
<meta charset="utf-8">
<title>Brisk Mend — Protection &amp; Repair</title>
<link href="https://fonts.googleapis.com/css2?family=Open+Sans:wght@300;400;600;700&display=swap" rel="stylesheet">
<style>
:root{
  --brand:#34a6d7;
  --brand-dark:#2587b4;
  --brand-deep:#1f78a3;
  --ink:#333b40;
  --muted:#7b8489;
  --light:#f2f5f7;
  --white:#ffffff;
  --dark:#22282c;
}
*{box-sizing:border-box;margin:0;padding:0}
html,body{width:684px;height:1200px;overflow:hidden}
body{font-family:"Open Sans",Arial,sans-serif;color:var(--ink);background:var(--white)}
.page{position:relative;width:684px;height:1200px}

/* header */
.site-header{height:64px;display:flex;align-items:center;justify-content:space-between;padding:0 34px 0 52px;background:var(--white)}
.brand{display:flex;align-items:center;gap:8px;font-weight:600;font-size:17px;color:var(--brand)}
.brand-mark{width:20px;height:20px;background:var(--brand)}
.main-nav{display:flex;gap:24px;font-size:9px;color:var(--ink)}
.main-nav a{text-decoration:none;color:inherit;padding:6px 6px}
.main-nav a.active{color:var(--brand);border-bottom:2px solid var(--brand)}

/* hero */
.hero{position:relative;height:278px;overflow:hidden}
.hero-photo{position:absolute;inset:0;background:linear-gradient(100deg,#8d959b 0%,#c7ccd0 35%,#aeb4b8 60%,#7d858b 100%)}
.hero-copy{position:absolute;left:28px;top:22px;color:var(--white)}
.hero-title{font-weight:300;font-size:34px;line-height:1;letter-spacing:-.5px}
.hero-points{list-style:none;margin-top:8px;font-size:12px;line-height:15px;font-weight:600;text-shadow:0 1px 2px rgba(0,0,0,.35)}
.btn-quote{display:inline-block;margin-top:22px;background:var(--dark);color:var(--white);font-size:9px;padding:6px 10px;border-radius:2px;text-decoration:none}
.hero-price{position:absolute;left:400px;top:30px;color:var(--white);font-size:25px;font-weight:600;white-space:nowrap}
.hero-dots{position:absolute;left:28px;bottom:12px;display:flex;gap:4px}
.hero-dots span{width:5px;height:5px;border-radius:50%;background:rgba(255,255,255,.6)}
.hero-dots span.on{background:var(--white)}

.plan-table{position:absolute;left:400px;top:70px;width:240px;background:var(--white);box-shadow:0 3px 10px rgba(0,0,0,.25);font-size:6px}
.plan-row{display:grid;grid-template-columns:75px 1fr 1fr 1fr;align-items:center;border-bottom:1px solid #e3e7ea;height:13px}
.plan-row span{text-align:center}
.plan-row span:first-child{text-align:left;padding-left:5px;color:var(--ink)}
.plan-head{height:32px;border-bottom:none}
.plan-col{display:flex;flex-direction:column;align-items:center;gap:2px}
.plan-name{background:var(--brand);color:var(--white);width:48px;padding:1px 0;font-weight:600}
.plan-cost{background:#e9eef1;width:48px;font-size:9px;font-weight:700;color:var(--ink);padding:2px 0}
.plan-col.featured .plan-name{background:var(--brand-dark)}
.tick{color:var(--brand);font-weight:700}
.cross{color:var(--ink);font-weight:700}
.plan-select{display:grid;grid-template-columns:75px 1fr 1fr 1fr;height:18px;align-items:center}
.plan-select span{justify-self:center;background:#e9eef1;color:var(--brand-dark);font-size:5.5px;padding:2px 4px;border-radius:2px}
.plan-note{background:var(--brand);color:var(--white);font-size:5.5px;padding:3px 5px}

/* repair services */
.services{height:228px;background:var(--white);padding-top:10px}
.section-title{text-align:center;font-weight:400;font-size:22px;color:var(--brand)}
.service-cards{display:flex;justify-content:center;gap:12px;margin-top:12px}
.service-card{width:182px;box-shadow:0 2px 6px rgba(0,0,0,.15)}
.service-photo{height:116px}
.service-photo.liquid{background:linear-gradient(135deg,#6f7a80,#c9d1d6 60%,#8a9499)}
.service-photo.mechanical{background:linear-gradient(135deg,#3d4a56,#7f8f9c 55%,#2e3943)}
.service-photo.accidental{background:linear-gradient(135deg,#b8a898,#e0d8cf 55%,#9a8c80)}
.service-label{background:var(--brand);color:var(--white);font-size:10px;padding:8px 10px}

/* about band */
.about-band{position:relative;height:224px;background:linear-gradient(180deg,#3aaee0,var(--brand) 60%,#2f9bcb);color:var(--white);overflow:hidden}
.about-copy{position:absolute;left:52px;top:24px;width:270px}
.about-title{font-weight:400;font-size:22px}
.about-lead{font-size:6px;line-height:8px;margin-top:4px;opacity:.85}
.about-points{list-style:none;margin-top:10px;font-size:8px;line-height:11px;font-weight:600}
.about-points li::before{content:"•";margin-right:5px}
.about-copy .btn-quote{margin-top:14px}
.about-photo{position:absolute;left:310px;top:24px;width:350px;height:196px;background:radial-gradient(ellipse at 45% 60%,#1a1f24 0%,#33414c 45%,rgba(52,166,215,0) 72%)}

/* reviews */
.reviews{position:relative;height:232px;overflow:hidden}
.reviews-photo{position:absolute;inset:0;background:linear-gradient(180deg,#2f3a40,#4f5b61 50%,#39444a)}
.reviews .section-title{position:relative;color:var(--white);padding-top:14px}
.review-phones{position:relative;display:flex;justify-content:center;gap:30px;margin-top:14px}
.phone{width:134px;height:170px;background:#1b1f22;border-radius:16px 16px 0 0;padding:22px 9px 0;box-shadow:0 2px 8px rgba(0,0,0,.4)}
.phone-screen{background:var(--white);height:100%;padding:12px 10px;text-align:center}
.stars{color:#f5b400;font-size:10px;letter-spacing:1px}
.review-text{font-size:6.5px;line-height:9px;color:var(--muted);margin-top:6px}
.review-name{font-size:6.5px;color:var(--brand);margin-top:6px}

/* footer */
.site-footer{height:150px;background:var(--brand);color:var(--white);display:grid;grid-template-columns:repeat(4,1fr);padding:18px 22px 0 52px}
.footer-title{font-weight:400;font-size:15px}
.footer-links{list-style:none;margin-top:8px;font-size:6px;line-height:9.5px;opacity:.9}
.legal-bar{height:24px;background:var(--brand-deep);color:var(--white);display:flex;align-items:center;justify-content:space-between;padding:0 22px 0 52px;font-size:5.5px}
.social{display:flex;gap:4px}
.social span{width:10px;height:10px;border-radius:50%;background:var(--white);opacity:.9}
</style>
</head>
<body>
<div class="page">

  <header class="site-header">
    <div class="brand"><span class="brand-mark"></span>Brisk Mend</div>
    <nav class="main-nav">
      <a class="active" href="#">Home</a>
      <a href="#">About us</a>
      <a href="#">Protection</a>
      <a href="#">Repair</a>
      <a href="#">Contact us</a>
    </nav>
  </header>

  <section class="hero">
    <div class="hero-photo" role="img" aria-label="Hand holding a smartphone over a blurred background"></div>
    <div class="hero-copy">
      <h1 class="hero-title">Peace of mind</h1>
      <ul class="hero-points">
        <li>Covers phones up to 3 years old</li>
        <li>Next-day claims resolution</li>
        <li>Unlimited claims</li>
      </ul>
      <a class="btn-quote" href="#">Get Quote</a>
    </div>
    <div class="hero-price">from $5.99 a month</div>

    <div class="plan-table">
      <div class="plan-row plan-head">
        <span></span>
        <span class="plan-col"><span class="plan-name">Basic</span><span class="plan-cost">$8.75</span></span>
        <span class="plan-col featured"><span class="plan-name">Plus</span><span class="plan-cost">$12.50</span></span>
        <span class="plan-col"><span class="plan-name">Elite</span><span class="plan-cost">$15.99</span></span>
      </div>
      <div class="plan-row"><span>Accidental damage</span><span class="tick">✓</span><span class="tick">✓</span><span class="tick">✓</span></div>
      <div class="plan-row"><span>Mechanical breakdown</span><span class="tick">✓</span><span class="tick">✓</span><span class="tick">✓</span></div>
      <div class="plan-row"><span>Monthly payments</span><span class="cross">✕</span><span class="tick">✓</span><span class="tick">✓</span></div>
      <div class="plan-row"><span>Excess per claim</span><span>$50</span><span>$25</span><span>Unlimited</span></div>
      <div class="plan-row"><span>Yearly claim limit</span><span>1 per year</span><span>2 per year</span><span>Unlimited</span></div>
      <div class="plan-row"><span>Cancellation policy</span><span>Cancel any time</span><span>Cancel any time</span><span>Cancel any time</span></div>
      <div class="plan-select"><span></span><span>Select plan</span><span>Select plan</span><span>Select plan</span></div>
      <div class="plan-note">Prices shown are monthly — easy plans for every phone</div>
    </div>

    <div class="hero-dots"><span class="on"></span><span></span><span></span></div>
  </section>

  <section class="services">
    <h2 class="section-title">Our Repair Services</h2>
    <div class="service-cards">
      <article class="service-card">
        <div class="service-photo liquid" role="img" aria-label="Person walking with an umbrella in the rain"></div>
        <div class="service-label">Liquid &amp; water damage</div>
      </article>
      <article class="service-card">
        <div class="service-photo mechanical" role="img" aria-label="Opened smartphone showing its circuit board"></div>
        <div class="service-label">Mechanical breakdowns</div>
      </article>
      <article class="service-card">
        <div class="service-photo accidental" role="img" aria-label="Hand holding a phone with a cracked screen"></div>
        <div class="service-label">Accidental damage</div>
      </article>
    </div>
  </section>

  <section class="about-band">
    <div class="about-copy">
      <h2 class="about-title">Brisk Mend</h2>
      <p class="about-lead">Bay area repair experts now offering full protection plans for phones and tablets, built for people and teams.</p>
      <ul class="about-points">
        <li>Cracked screens &amp; accidental damage</li>
        <li>One plan covers all of your devices</li>
        <li>Low monthly price</li>
        <li>Next-day claims resolution</li>
      </ul>
      <a class="btn-quote" href="#">Get Quote</a>
    </div>
    <div class="about-photo" role="img" aria-label="Shattered tablet and a hand holding a broken phone"></div>
  </section>

  <section class="reviews">
    <div class="reviews-photo" role="img" aria-label="Blurred city street with people walking"></div>
    <h2 class="section-title">Our Customer Reviews</h2>
    <div class="review-phones">
      <div class="phone">
        <div class="phone-screen">
          <div class="stars">★★★★★</div>
          <p class="review-text">"Super quick! My screen was fixed the same day and my plan covered all of it."</p>
          <p class="review-name">— Dana Reyes</p>
        </div>
      </div>
      <div class="phone">
        <div class="phone-screen">
          <div class="stars">★★★★★</div>
          <p class="review-text">"Very easy claim, friendly staff and my tablet came back like new within a day."</p>
          <p class="review-name">— Dana Reyes</p>
        </div>
      </div>
    </div>
  </section>

  <footer class="site-footer">
    <div>
      <h3 class="footer-title">Quick Links</h3>
      <ul class="footer-links"><li>Home</li><li>About us</li><li>Protection</li><li>Repair</li><li>Contact us</li></ul>
    </div>
    <div>
      <h3 class="footer-title">Our Services</h3>
      <ul class="footer-links"><li>Liquid &amp; water damage</li><li>Cracked screens</li><li>Accidental damage</li><li>Mechanical breakdowns</li><li>Battery problems</li></ul>
    </div>
    <div>
      <h3 class="footer-title">My Account</h3>
      <ul class="footer-links"><li>Login</li><li>My orders</li><li>My devices</li><li>Claim status</li><li>Sign up</li><li>Update my details</li><li>Logout</li></ul>
    </div>
    <div>
      <h3 class="footer-title">Protection</h3>
      <ul class="footer-links"><li>Coverage</li><li>File a claim</li><li>Corporate plans</li><li>Prices</li><li>FAQ</li><li>Terms &amp; conditions</li></ul>
    </div>
  </footer>
  <div class="legal-bar">
    <span>© 2024 Brisk Mend. All rights reserved.</span>
    <div class="social"><span></span><span></span><span></span><span></span></div>
  </div>

</div>
</body>
</html>
```